Wordpress Web Design Project for Upmarket Trendy Modern Travel Agency

We are a independent travel agency that does not offer online bookings (at this stage). We offer quality service and this needs to be reflected somehow in the design i.e. good old fashioned service.

Looking for wordpress Design for Travel Site

Company Name Voyage Harbour

www.voyageharbour-example.com.au

Looking for something outside the box and not from layout lagoon.

Something uniquely different !

Reason: Just have not see the right design.

Target Market(s)

Everyone

Industry/Entity Type

Travel

Requirements
Must have
• 1. Booking form
2. Seo friendly layout
3. Everything should be managed from wordpress admin

```html
<!DOCTYPE html>
<html lang="en">
<head>
<meta charset="utf-8">
<title>Voyage Harbour – Realize Your Travel Dreams With Us</title>
<link rel="stylesheet" href="https://fonts.googleapis.com/css2?family=Arimo:wght@400;700&family=Oswald:wght@500&display=swap">
<style>
:root{
  --brand-navy:#0d4a78;
  --link-blue:#1a6fa8;
  --sky:#1b8fd8;
  --accent-orange:#f07d14;
  --price-cyan:#2aa9d6;
  --button:#6ecbf3;
  --text:#1c1c1c;
  --panel:#e3e5ec;
  --panel-border:#d3d6de;
  --page-top:#d9dbe3;
  --page-bottom:#eff0f4;
  --footer:#dcdde4;
}
*{box-sizing:border-box;margin:0;padding:0}
html,body{width:1200px;height:1122px;overflow:hidden}
body{font-family:"Arimo",Arial,sans-serif;color:var(--text);position:relative;
  background:linear-gradient(to bottom,#fff 0,#fff 80px,#e9eaee 135px,var(--page-top) 140px,var(--page-bottom) 700px,var(--page-bottom) 100%);}
.abs{position:absolute}
.brand{left:113px;top:26px;font-size:29px;font-weight:700;color:var(--brand-navy);letter-spacing:1px;white-space:nowrap}
.brand-dot{left:370px;top:18px;width:7px;height:7px;border-radius:50%;background:var(--brand-navy)}
.tagline{left:380px;top:72px;font-size:11px;font-weight:700;color:var(--sky)}
.nav{left:620px;top:82px;display:flex;gap:7px}
.nav a{display:block;height:23px;line-height:23px;text-align:center;font-size:11px;font-weight:700;color:#111;text-decoration:none;
  background:linear-gradient(#f4f4f6,#dcdde2)}
.nav a.active{background:linear-gradient(#2f9ff0,#1584de);color:#fff}
.photo{border:3px solid #fff;box-shadow:0 2px 6px rgba(0,0,0,.25)}
.hero{left:322px;top:113px;width:533px;height:245px;border:none;
  background:radial-gradient(ellipse at 50% 55%,#5f8a78 0,#6fc3a8 35%,#9fe0c6 70%,#5fb896 100%);box-shadow:0 0 12px rgba(255,255,255,.8)}
.offer-title{width:190px;text-align:center;font-size:13px;font-weight:700;top:415px}
.offer-title .lead{color:var(--accent-orange)}
.offer-title .place{color:var(--brand-navy)}
.offer-img{width:190px;height:190px;top:442px}
.price{width:190px;text-align:center;top:646px;font-size:16px;line-height:26px}
.price b{font-family:"Oswald",sans-serif;font-weight:500;font-size:22px;color:var(--price-cyan)}
.price sup{font-size:13px}
.blurb{width:200px;text-align:center;font-size:10.2px;line-height:11.2px;top:682px}
.btn{display:block;height:16px;line-height:16px;width:74px;text-align:center;font-size:10px;color:#1c3a55;background:var(--button);text-decoration:none}
.headline{left:312px;top:775px;font-size:24px;font-weight:700;color:var(--link-blue);white-space:nowrap}
.map{left:314px;top:816px;width:227px;height:147px;background:#5cb8e8}
.copy{font-size:10px;line-height:11.3px}
.side-box{left:741px;width:156px;background:var(--panel);border:1px solid var(--panel-border)}
.side-box h3{position:absolute;left:13px;font-size:11px;font-weight:700;color:var(--brand-navy)}
.dest{position:absolute;left:9px;top:37px;list-style:none;font-size:10px}
.dest li{height:12.2px;line-height:12.2px}
.dest li::before{content:"✧";color:#6aa2c8;font-size:7px;margin-right:4px;vertical-align:1px}
.dest a{color:var(--link-blue)}
.credit{position:absolute;left:0;width:154px;text-align:center;font-size:10px;line-height:11px;color:var(--link-blue);text-decoration:underline}
.footer{left:0;top:1097px;width:1200px;height:25px;background:var(--footer);text-align:center;font-size:8px;line-height:9.5px;padding-top:4px}
.footer a{color:var(--sky);text-decoration:none}
</style>
</head>
<body>

<header>
  <div class="abs brand">VOYAGE HARBOUR</div>
  <div class="abs brand-dot"></div>
  <p class="abs tagline">Realize Your Travel Dreams With Us</p>
  <nav class="abs nav">
    <a class="active" href="#" style="width:63px">Home</a>
    <a href="#" style="width:75px">Booking</a>
    <a href="#" style="width:78px">Contacts</a>
  </nav>
</header>

<section class="showcase" aria-label="Destination gallery">
  <div class="abs photo" role="img" aria-label="Rocky coastline photo" style="left:175px;top:155px;width:70px;height:120px;transform:rotate(-8deg);background:linear-gradient(#5b8fb8,#3a6d94)"></div>
  <div class="abs photo" role="img" aria-label="Sunset with kangaroo silhouette photo" style="left:215px;top:95px;width:110px;height:115px;transform:rotate(12deg);background:linear-gradient(#f5b21e,#e06a0a 70%,#3a2a10)"></div>
  <div class="abs photo" role="img" aria-label="City skyline by the water photo" style="left:232px;top:200px;width:92px;height:100px;transform:rotate(-4deg);background:linear-gradient(#2d4fb8,#6f88c9 60%,#1a2c5a)"></div>
  <div class="abs photo" role="img" aria-label="Red desert rocks photo" style="left:205px;top:270px;width:110px;height:110px;transform:rotate(-14deg);background:linear-gradient(#6fa4d8,#d77b30 55%,#8a3a18)"></div>
  <div class="abs photo" role="img" aria-label="Coastal cliffs photo" style="left:855px;top:100px;width:90px;height:135px;transform:rotate(-6deg);background:linear-gradient(#8fbfe6,#3d6f9a 55%,#2a4e6e)"></div>
  <div class="abs photo" role="img" aria-label="Skydivers over the sea photo" style="left:935px;top:150px;width:80px;height:110px;transform:rotate(-10deg);background:linear-gradient(#3c8fdc,#9ad0f0 70%,#2d7ac0)"></div>
  <div class="abs photo" role="img" aria-label="City towers at night photo" style="left:855px;top:235px;width:100px;height:130px;transform:rotate(6deg);background:linear-gradient(#2b3f8a,#c08a30 70%,#5a3e10)"></div>
  <div class="abs photo" role="img" aria-label="Diver over coral reef photo" style="left:925px;top:270px;width:95px;height:120px;transform:rotate(28deg);background:linear-gradient(#2c8ad0,#1a5a98 60%,#7a4a40)"></div>
  <div class="abs photo hero" role="img" aria-label="Sea turtle swimming in clear green water"></div>
</section>

<main>
  <article class="offer">
    <h2 class="abs offer-title" style="left:314px"><span class="lead">Hot Offer:</span> <span class="place">Barbadoes</span></h2>
    <div class="abs offer-img" role="img" aria-label="Palm trees leaning over a white sand beach" style="left:314px;background:linear-gradient(#3a78c8 0,#9cc8ee 45%,#3f7a3a 55%,#e8dcc0 85%)"></div>
    <p class="abs price" style="left:314px">From $<b>595</b><sup>*</sup></p>
    <p class="abs blurb" style="left:309px">Lorem ipsum dolor sit amet, consectetur adipiscing elit. Etiam pharetra, tellus sit amet congue vulputate, nisi erat iaculis nibh, vitae feugiat sapien.</p>
    <a class="abs btn" href="#" style="left:373px;top:736px">read more</a>
  </article>

  <article class="offer">
    <h2 class="abs offer-title" style="left:525px"><span class="lead">Best Price:</span><span class="place">Tahiti</span></h2>
    <div class="abs offer-img" role="img" aria-label="Bamboo beach hut with hammock by the sea" style="left:525px;background:linear-gradient(#2b6fc8 0,#6fb0e8 40%,#c8a060 60%,#efe4c8 90%)"></div>
    <p class="abs price" style="left:525px">From $<b>1225</b><sup>*</sup></p>
    <p class="abs blurb" style="left:520px">Aenean sollicitudin imperdiet arcu, vitae dignissim est posuere id. Duis placerat justo eu nunc interdum ultrices. Phasellus elit dolor, porttitor id.</p>
    <a class="abs btn" href="#" style="left:583px;top:736px">read more</a>
  </article>

  <section class="planning">
    <h1 class="abs headline">Where Are You Planning To Go?</h1>
    <div class="abs map" role="img" aria-label="World map in white on light blue"></div>
    <div class="abs copy" style="left:549px;top:815px;width:168px">
      <p>Lorem ipsum dolor sit amet, consectetur adipiscing elit. Etiam pharetra, tellus sit amet congue vulputate, nisi erat iaculis nibh, vitae feugiat sapien ante eget mauris. Cras elit nisl, rhoncus nec iaculis ultricies, feugiat eget sapien. Pellentesque ac felis tellus.</p>
      <p style="margin-top:10px">Aenean sollicitudin imperdiet arcu, vitae dignissim est posuere id. Duis placerat justo eu nunc interdum ultrices. Phasellus elit dolor, porttitor id consectetur sit amet, posuere id</p>
    </div>
    <p class="abs copy" style="left:312px;top:971px">magna.</p>
    <p class="abs copy" style="left:312px;top:992px;width:410px">Fusce ornare elit nisl, feugiat bibendum lorem. Vivamus pretium dictum sem vel laoreet. In fringilla pharetra purus, semper vulputate ligula cursus in. Donec at nunc nec dui laoreet porta eu eu ipsum. Sed eget lacus sit amet risus elementum dictum. Pellentesque sit amet imperdiet nunc. Aenean tellus mi, adipiscing sit amet laoreet eget, lobortis quis nisl. Quisque volutpat urna orci, id gravida nisi. Nullam posuere interdum est sit amet aliquam.</p>
    <a class="abs btn" href="#" style="left:312px;top:1058px">read more</a>
  </section>
</main>

<aside>
  <section class="abs side-box" style="top:409px;height:210px">
    <h3 style="top:14px">Hot Destinations</h3>
    <ul class="dest">
      <li><a href="#">Acapulco</a></li><li><a href="#">Aruba</a></li><li><a href="#">Bahamas</a></li>
      <li><a href="#">Bali</a></li><li><a href="#">Barbados</a></li><li><a href="#">Belize</a></li>
      <li><a href="#">Bermuda</a></li><li><a href="#">Cancun</a></li><li><a href="#">Cap Cana</a></li>
      <li><a href="#">Costa Rica</a></li><li><a href="#">Cozumel</a></li><li><a href="#">Curacao</a></li>
      <li><a href="#">Hawaii</a></li>
    </ul>
  </section>

  <section class="abs side-box" style="top:627px;height:207px">
    <h3 style="top:13px">This Month Popular</h3>
    <div class="abs" role="img" aria-label="Longtail boat on a turquoise shore" style="left:10px;top:40px;width:134px;height:100px;background:linear-gradient(#7ec6e8,#3fb8c8 55%,#e8e0c8 90%)"></div>
    <p class="credit" style="top:148px">Image: sandline /<br>OpenStockFrames.net</p>
    <a class="abs btn" href="#" style="left:40px;top:175px">read more</a>
  </section>

  <section class="abs side-box" style="top:842px;height:247px">
    <h3 style="top:13px">Our Mission</h3>
    <div class="abs" role="img" aria-label="Couple walking hand in hand along the beach" style="left:9px;top:40px;width:137px;height:168px;background:linear-gradient(#9bb8cc,#6f9ab4 40%,#c8d4da 75%,#b8a88e)"></div>
    <a class="abs btn" href="#" style="left:40px;top:215px">read more</a>
  </section>
</aside>

<footer class="abs footer">
  <a href="#">Terms of use</a> | <a href="#">Privacy Policy</a> | <a href="#">Advertise With Us</a><br>All Rights Reserved.
</footer>

</body>
</html>
```